Business Card Design Project

New business card design front and back for IT company that does network support and web design.
Calloway IT
Doug Calloway
Managing Director
PO Box 918 Brinsley VIC 3421
doug@callowayit.example
www.callowayit.example

Industry/Entity Type

Business

```html
<!DOCTYPE html>
<html lang="en">
<head>
<meta charset="utf-8">
<title>Calloway IT — Business Card Front and Back</title>
<link href="https://fonts.googleapis.com/css2?family=Lato:wght@400;700&display=swap" rel="stylesheet">
<style>
  :root {
    --stage: #e6e8ea;
    --brand-blue: #2eaedb;
    --brand-blue-deep: #1f9ccb;
    --ink-dark: #2b2b2d;
    --card-white: #fbfbfb;
    --text-grey: #3a3a3c;
    --white: #ffffff;
  }
  * { box-sizing: border-box; margin: 0; padding: 0; }
  html, body {
    width: 1200px;
    height: 900px;
    overflow: hidden;
    background: var(--stage);
    font-family: "Lato", Arial, sans-serif;
  }
  .stage {
    position: relative;
    width: 1200px;
    height: 900px;
  }
  .card {
    position: absolute;
    left: 285px;
    width: 630px;
    height: 360px;
    border-radius: 4px;
    overflow: hidden;
    box-shadow: 0 6px 18px rgba(0,0,0,0.12);
  }

  /* Front */
  .card--front {
    top: 70px;
    background: var(--brand-blue);
    display: flex;
    flex-direction: column;
    align-items: center;
    justify-content: center;
  }
  .card--front .sheen {
    position: absolute;
    inset: 0;
    width: 100%;
    height: 100%;
  }
  .front-lockup {
    position: relative;
    display: flex;
    flex-direction: column;
    align-items: flex-start;
  }
  .front-name {
    display: flex;
    align-items: center;
    gap: 16px;
    color: var(--white);
    font-weight: 700;
    font-size: 58px;
    letter-spacing: 1px;
    line-height: 1;
  }
  .front-name .mark-square {
    width: 34px;
    height: 34px;
    background: var(--ink-dark);
  }
  .tagline {
    margin-top: 16px;
    display: flex;
    align-items: stretch;
    background: var(--brand-blue-deep);
    color: var(--white);
    font-weight: 700;
    font-size: 20px;
    letter-spacing: 0.5px;
  }
  .tagline .tagline-bar {
    width: 7px;
    background: var(--ink-dark);
  }
  .tagline .tagline-text {
    padding: 5px 12px 6px 10px;
  }

  /* Back */
  .card--back {
    top: 470px;
    background: var(--card-white);
    padding: 42px 0 0 60px;
  }
  .back-name {
    color: var(--brand-blue);
    font-weight: 700;
    font-size: 40px;
    letter-spacing: 1px;
    line-height: 1;
  }
  .contact-block {
    margin-top: 36px;
    padding-left: 20px;
    border-left: 2px solid var(--brand-blue);
    color: var(--text-grey);
    font-size: 17px;
    line-height: 1.45;
  }
  .person {
    font-size: 23px;
    letter-spacing: 0.5px;
    margin-bottom: 10px;
  }
  .person .role {
    font-size: 17px;
    margin-left: 6px;
    padding-left: 8px;
    border-left: 1px solid var(--text-grey);
  }
  .contact-line .label {
    display: inline-block;
    width: 22px;
    color: var(--brand-blue);
    font-weight: 700;
    font-style: italic;
  }
  .website {
    margin-top: 14px;
    color: var(--text-grey);
    font-size: 17px;
  }
  .website .domain { color: var(--brand-blue); }
</style>
</head>
<body>
<main class="stage">

  <section class="card card--front" aria-label="Business card front">
    <svg class="sheen" viewBox="0 0 630 360" preserveAspectRatio="none" aria-hidden="true">
      <path d="M0 360 C120 200 260 80 630 0 L630 360 Z" fill="#ffffff" opacity="0.05"/>
      <path d="M380 360 C430 230 520 150 630 110 L630 360 Z" fill="#ffffff" opacity="0.05"/>
    </svg>
    <div class="front-lockup">
      <h1 class="front-name"><span class="mark-square"></span>CALLOWAY IT</h1>
      <p class="tagline"><span class="tagline-bar"></span><span class="tagline-text">IT Solutions For Your Business</span></p>
    </div>
  </section>

  <section class="card card--back" aria-label="Business card back">
    <h2 class="back-name">CALLOWAY IT</h2>
    <div class="contact-block">
      <p class="person">DOUG CALLOWAY<span class="role">MANAGING DIRECTOR</span></p>
      <p class="contact-line"><span class="label">t</span>0400 555 019</p>
      <p class="contact-line"><span class="label">e</span>doug@callowayit.example</p>
      <p class="contact-line">PO Box 918 Brinsley VIC 3421</p>
    </div>
    <p class="website">www.<span class="domain">callowayit</span>.example</p>
  </section>

</main>
</body>
</html>
```